New Business Card Design Project

Use the flyer uploaded and website www.brightoakbuilders.com for inspiration.
List Our Services on Backside of business cards
Martin Hollis
Harborline Renovations Inc.
Licensed General Contractors
858-471-9063

Contact Information for Business Card

Use the flyer uploaded and website www.brightoakbuilders.com for inspiration. List Our Services on Backside of business cards Martin Hollis Harborline Renovations Inc. Licensed General Contractors 858-471-9063

```html
<!DOCTYPE html>
<html lang="en">
<head>
<meta charset="utf-8">
<title>Harborline Renovations – Business Cards</title>
<link href="https://fonts.googleapis.com/css2?family=Crimson+Pro:wght@400;600;700&display=swap" rel="stylesheet">
<style>
  :root {
    --bg: #3a3a3c;
    --card-black: #111111;
    --card-white: #ffffff;
    --card-grey: #e6e6e6;
    --accent-blue: #2a8fd0;
    --ink: #1a1a1a;
    --line-white: #ffffff;
  }
  * { margin: 0; padding: 0; box-sizing: border-box; }
  html, body { width: 1200px; height: 900px; overflow: hidden; background: var(--bg); }
  body { font-family: "Crimson Pro", "Times New Roman", serif; color: var(--ink); position: relative; }

  .card {
    position: absolute;
    left: 250px;
    width: 700px;
    height: 400px;
    background: linear-gradient(135deg, var(--card-white) 55%, var(--card-grey) 100%);
    box-shadow: 0 10px 24px rgba(0,0,0,.45);
    overflow: hidden;
  }
  .card--back { top: 35px; }
  .card--front { top: 465px; }
  .card__shapes { position: absolute; inset: 0; }

  .brand-name {
    position: absolute;
    color: var(--card-white);
    font-weight: 400;
    letter-spacing: 2px;
    text-transform: uppercase;
    white-space: nowrap;
  }
  .card--back .brand-name { left: 48px; top: 176px; font-size: 24px; line-height: 30px; }
  .card--front .brand-name { right: 36px; top: 148px; font-size: 22px; }

  .services {
    position: absolute;
    right: 34px;
    top: 86px;
    text-align: right;
    font-size: 19px;
    line-height: 22px;
  }
  .services__title { color: var(--accent-blue); font-weight: 600; font-size: 20px; letter-spacing: .5px; margin-bottom: 2px; }
  .services__list { list-style: none; }

  .guarantee {
    position: absolute;
    right: 40px;
    bottom: 30px;
    font-weight: 700;
    font-size: 24px;
  }

  .contact { position: absolute; left: 40px; top: 262px; }
  .contact__name { color: var(--accent-blue); font-weight: 600; font-size: 28px; letter-spacing: 1px; text-transform: uppercase; line-height: 32px; }
  .contact__line { font-size: 20px; line-height: 23px; }

  .reach { position: absolute; right: 46px; top: 262px; }
  .reach__cta { font-weight: 700; font-size: 22px; }
  .reach__phone { display: flex; align-items: center; gap: 10px; font-size: 38px; line-height: 42px; }
  .reach__icon { width: 30px; height: 30px; }
  .reach__web { font-size: 19px; }
</style>
</head>
<body>

<section class="card card--back" aria-label="Business card back">
  <svg class="card__shapes" viewBox="0 0 700 400" preserveAspectRatio="none">
    <polygon points="0,0 700,0 700,52 410,66 160,400 0,400" fill="var(--card-black)"/>
    <polyline points="700,40 400,54 146,400" fill="none" stroke="var(--line-white)" stroke-width="2"/>
  </svg>
  <div class="brand-name">Harborline<br>Renovations</div>

  <div class="services">
    <h2 class="services__title">OUR SERVICES</h2>
    <ul class="services__list">
      <li>Remodel - Kitchen &amp; Bath</li>
      <li>Painting - Interior &amp; Exterior</li>
      <li>Flooring - Carpet, Vinyl, Wood</li>
      <li>Window &amp; Door Replacement</li>
      <li>Plumbing - Repairs &amp; Upgrades</li>
      <li>Energy - Efficient Upgrades</li>
      <li>Deck &amp; Patio Construction</li>
      <li>Water &amp; Mold Damage</li>
      <li>Garage Renovation</li>
    </ul>
  </div>
  <p class="guarantee">Our Services Are 100% Guaranteed</p>
</section>

<section class="card card--front" aria-label="Business card front">
  <svg class="card__shapes" viewBox="0 0 700 400" preserveAspectRatio="none">
    <polygon points="0,0 700,0 700,218 238,228 0,240" fill="var(--card-black)"/>
    <polyline points="0,222 236,214 700,206" fill="none" stroke="var(--line-white)" stroke-width="2"/>
    <line x1="236" y1="214" x2="560" y2="0" stroke="var(--line-white)" stroke-width="2"/>
  </svg>
  <div class="brand-name">Harborline Renovations</div>

  <div class="contact">
    <h1 class="contact__name">Martin Hollis</h1>
    <p class="contact__line">Harborline Renovations Inc.</p>
    <p class="contact__line">Licensed General Contractors</p>
  </div>

  <div class="reach">
    <p class="reach__cta">Call/Text Or Book Online</p>
    <p class="reach__phone">
      <svg class="reach__icon" viewBox="0 0 24 24" aria-hidden="true">
        <path d="M6.6 10.8a15.1 15.1 0 0 0 6.6 6.6l2.2-2.2a1 1 0 0 1 1-.25 11.4 11.4 0 0 0 3.6.57 1 1 0 0 1 1 1V20a1 1 0 0 1-1 1A17 17 0 0 1 3 4a1 1 0 0 1 1-1h3.5a1 1 0 0 1 1 1c0 1.25.2 2.45.57 3.570a1 1 0 0 1-.25 1z" fill="var(--ink)"/>
        <path d="M14 3a7 7 0 0 1 7 7M14 6.5a3.5 3.5 0 0 1 3.5 3.5" fill="none" stroke="var(--ink)" stroke-width="1.8" stroke-linecap="round"/>
      </svg>
      858-471-9063
    </p>
    <p class="reach__web">www.brightoakbuilders.com</p>
  </div>
</section>

</body>
</html>
```